Landlord Handbook for real estate agency clients

We are a boutique Real Estate Agency that specializes in Property Management (Rentals) Located on Sydney's Northern Beaches.

We are putting together a property owners handbook that informs them about being a landlord, setting up their property for rent, local legislation on leasing properties, the services we offer and what makes us a great choice to manage their property.
Ultimately this is designed to answer new landlords FAQs and sell our agency as the best choice for them.

We want this handbook to be simple, clear and styled to match our existing website. wwww.harbourlinkrealty.com.au

We have supplied some images, screen shots of our Landlord Portal service offered. All words and index are provided in the word.doc
The services we want to feature are:
Our Landlord Portal
Our Service Guarantee
Quality Tenant Database
6 Month Property Reports

I would like the brochure to be around 16-20 A4 pages with some of the images provided and/or any other images you would like to add.

An example of a similar owners handbook can be found here: http://www.zentro.com.au/marsh_kettleby_poh/
But I would like something a little more modern and matched to our website design.

I would like a print ready PDF version of document as well as an editable Photoshop copy and AI copy.

Thank you and I look forward t your designs!
Tom.

Target Market(s)

30-65YO Men and women that own investment properties on Sydney's Northern Beaches

Industry/Entity Type

Real Estate

Font styles to use
Serif

Requirements
Must have
• Must use one of the Town house images provided on the front cover to match our website www.harbourlinkrealty.com.au
• Index of details at the start.
• Use one or all of our screen shot images of the Landlord Portal to promote this feature within the landlord portal description in content.
Should not have
• Any images of foreign currency, landscapes or houses. We are based in Sydney Australia on the beach so we want to keep it local and use Australian images, currency, landscapes and houses.

```html
<!DOCTYPE html>
<html lang="en">
<head>
<meta charset="utf-8">
<title>Harbourlink Realty – Landlord Handbook Cover</title>
<link rel="stylesheet" href="https://fonts.googleapis.com/css2?family=Oswald:wght@300;400;500;600&family=Tinos:wght@400;700&display=swap">
<style>
  :root {
    --backdrop: #a7a7a7;
    --teal-deep: #146f80;
    --teal-mid: #1f8f9c;
    --teal-glow: #2aa6ad;
    --teal-strip: #1a8196;
    --sky: #4fb5d4;
    --garden: #3f6a4a;
    --night: #0b0b0b;
    --band: #141210;
    --white: #ffffff;
  }
  * { margin: 0; padding: 0; box-sizing: border-box; }
  html, body { width: 1200px; height: 978px; overflow: hidden; }
  body { background: var(--backdrop); position: relative; font-family: "Tinos", "Times New Roman", serif; color: var(--white); }

  .spread { position: absolute; left: 108px; top: 128px; width: 992px; height: 706px; display: flex; box-shadow: 0 6px 18px rgba(0,0,0,.25); }
  .page { position: relative; width: 496px; height: 100%; overflow: hidden; }

  /* Back cover */
  .back-cover__body {
    position: absolute; left: 0; top: 0; width: 100%; height: 562px;
    background: radial-gradient(ellipse at 52% 60%, var(--teal-glow) 0%, var(--teal-mid) 38%, var(--teal-deep) 100%);
  }
  .team-heading { position: absolute; top: 229px; width: 100%; text-align: center; font-family: "Oswald", sans-serif; font-weight: 500; font-size: 19px; letter-spacing: .3px; }
  .team-copy { position: absolute; top: 263px; left: 34px; right: 40px; text-align: center; font-size: 13.4px; line-height: 16px; }
  .brand-name { font-family: "Oswald", sans-serif; font-weight: 400; color: var(--white); letter-spacing: .5px; white-space: nowrap; }
  .back-cover .brand-name { position: absolute; right: 26px; top: 494px; font-size: 22px; }

  .contact-band { position: absolute; left: 0; bottom: 0; width: 100%; height: 144px; background: var(--night); padding: 19px 0 0 24px; }
  .contact-row { display: flex; align-items: center; gap: 18px; font-size: 12.5px; height: 26px; }
  .contact-row svg { width: 16px; height: 16px; flex: none; fill: var(--white); }
  .contact-row--phone { font-weight: 700; font-size: 25px; height: 34px; margin-bottom: 0; }

  /* Front cover */
  .front-cover__photo {
    position: absolute; left: 0; top: 0; width: 100%; height: 560px;
    background: linear-gradient(160deg, var(--sky) 0%, var(--garden) 100%);
  }
  .front-cover .brand-name { position: absolute; top: 58px; left: 0; width: 100%; text-align: center; font-size: 30px; }
  .headline-band { position: absolute; left: 0; top: 560px; width: 100%; height: 146px; background: var(--band); }
  .headline { position: absolute; top: 14px; width: 100%; text-align: center; font-family: "Oswald", sans-serif; font-weight: 300; font-size: 37px; line-height: 46px; letter-spacing: .3px; transform: scaleX(.87); }
  .web-strip { position: absolute; left: 0; bottom: 0; width: 100%; height: 30px; }
  .web-strip svg { position: absolute; inset: 0; }
  .web-strip span { position: absolute; left: 146px; top: 6px; font-size: 14px; letter-spacing: .4px; }
  .web-strip b { font-weight: 700; }
</style>
</head>
<body>
  <main class="spread">
    <section class="page back-cover">
      <div class="back-cover__body">
        <h2 class="team-heading">OUR BROAD TEAM:</h2>
        <p class="team-copy">Not only do we have a friendly, professional and efficient property management team – we also work closely with associated builders, accountants and mortgage brokers. So you have access to experienced professionals in all facets of property investment.<br>We work for you and its in our best interest that you get the best advice and service possible to get the most out of your investment.</p>
        <div class="brand-name">HARBOURLINK REALTY</div>
      </div>
      <div class="contact-band">
        <div class="contact-row contact-row--phone">
          <svg viewBox="0 0 24 24"><path d="M3 9c0-3 4-5 9-5s9 2 9 5v2h-5V8.5c-1.5-.5-6.5-.5-8 0V11H3zM6 12h12l2 7H4z"/></svg>
          0491 570 236
        </div>
        <div class="contact-row">
          <svg viewBox="0 0 24 24"><path d="M12 2a7 7 0 0 0-7 7c0 5 7 13 7 13s7-8 7-13a7 7 0 0 0-7-7zm0 9.5A2.5 2.5 0 1 1 12 6.5a2.5 2.5 0 0 1 0 5z"/></svg>
          PO Box 377 Collaroy, NSW 2097
        </div>
        <div class="contact-row">
          <svg viewBox="0 0 24 24"><path d="M2 5h20v14H2zm2 2v.5l8 5.5 8-5.5V7zm0 3v7h16v-7l-8 5.5z"/></svg>
          referrals@harbourlinkrealty.com.au
        </div>
        <div class="contact-row">
          <svg viewBox="0 0 24 24"><circle cx="12" cy="12" r="9" fill="none" stroke="#fff" stroke-width="2"/><path d="M3 12h18M12 3c-4 4.5-4 13.5 0 18M12 3c4 4.5 4 13.5 0 18" fill="none" stroke="#fff" stroke-width="1.6"/></svg>
          www.harbourlinkrealty.com.au
        </div>
      </div>
    </section>

    <section class="page front-cover">
      <div class="front-cover__photo" role="img" aria-label="Cover photograph: modern Northern Beaches townhouses with terraced gardens under a blue sky"></div>
      <div class="brand-name">HARBOURLINK REALTY</div>
      <div class="headline-band">
        <h1 class="headline">PROPERTY MANAGEMENT<br>DONE RIGHT!</h1>
        <div class="web-strip">
          <svg viewBox="0 0 496 30" preserveAspectRatio="none"><polygon points="48,0 496,0 496,30 31,30" fill="#1a8196"/></svg>
          <span>www.<b>harbourlinkrealty</b>.com.au</span>
        </div>
      </div>
    </section>
  </main>
</body>
</html>
```